New Business Card Design Project

We want a modern business card that catches the attention of other remodeling companies as well as homeowners. We would like it to be informative but still simple.

Target Market(s)

Residential and other Business's

Contact Information for Business Card

TrellBrix
Phone number is 5153927048
Address is
4817 SW 3rd Lane
Des Moines, Iowa 50313
email is trellbrixco@quamlet.com

Requirements
Must have
• Our tagline
• Honest | Professional | Affordable

```html
<!DOCTYPE html>
<html lang="en">
<head>
<meta charset="utf-8">
<title>TrellBrix Business Card</title>
<link rel="stylesheet" href="https://fonts.googleapis.com/css2?family=Montserrat:wght@400;700;800&display=swap">
<style>
  :root {
    --canvas: #e4e4e4;
    --ink-black: #1f1f1f;
    --brand-blue: #0f67c9;
    --brand-orange: #d2570f;
    --text-grey: #444444;
    --card-white: #ffffff;
  }
  * { box-sizing: border-box; margin: 0; padding: 0; }
  html, body {
    width: 1200px; height: 930px; overflow: hidden;
    background: var(--canvas);
    font-family: "Montserrat", sans-serif;
  }
  .card {
    position: absolute; left: 250px;
    width: 700px; height: 400px;
    border-radius: 24px; overflow: hidden;
  }
  .card-back {
    top: 40px; background: var(--ink-black);
    display: flex; align-items: center; justify-content: center;
  }
  .card-front { top: 490px; background: var(--card-white); }

  .wordmark {
    font-family: "Montserrat", sans-serif;
    font-weight: 800; color: var(--brand-blue);
    letter-spacing: 1px; line-height: 1; white-space: nowrap;
  }
  .card-back .wordmark { font-size: 84px; margin-top: 20px; }
  .card-front .wordmark { position: absolute; right: 48px; top: 50px; font-size: 44px; }

  .value-list {
    position: absolute; left: 52px; top: 128px;
    list-style: none; color: var(--brand-blue);
    font-size: 25px; font-weight: 400; line-height: 1.22;
  }
  .value-list li::before {
    content: "|"; color: var(--brand-orange); margin-right: 10px;
  }
  .value-list li:nth-child(2) { padding-left: 14px; }
  .value-list li:nth-child(3) { padding-left: 28px; }

  .person-name {
    position: absolute; left: 60px; top: 232px;
    font-size: 24px; font-weight: 700; letter-spacing: 1px;
    color: var(--brand-blue);
  }
  .person-name .surname { color: var(--brand-orange); }
  .divider {
    position: absolute; left: 60px; top: 264px;
    width: 590px; height: 2px; background: var(--brand-orange);
  }
  .person-role {
    position: absolute; left: 60px; top: 272px;
    font-size: 16px; color: var(--text-grey);
  }
  .contact-list {
    position: absolute; left: 60px; top: 304px;
    list-style: none; font-size: 16px; color: var(--text-grey);
    line-height: 1.45;
  }
  .contact-list li { display: flex; align-items: center; gap: 10px; }
  .contact-list svg { width: 14px; height: 14px; flex: none; }
  .address {
    position: absolute; right: 50px; top: 190px;
    text-align: right; font-size: 16px; color: var(--text-grey);
    line-height: 1.4;
  }
  .edge-band { position: absolute; left: 0; bottom: 0; width: 700px; height: 12px; }
</style>
</head>
<body>

<section class="card card-back" aria-label="Card back">
  <div class="wordmark">TrellBrix</div>
</section>

<section class="card card-front" aria-label="Card front">
  <div class="wordmark">TrellBrix</div>

  <ul class="value-list">
    <li>Honest</li>
    <li>Professional</li>
    <li>Affordable</li>
  </ul>

  <div class="address">4817 SW 3rd Lane<br>Des Moines, Iowa 50313</div>

  <div class="person-name">DEAN <span class="surname">WHITFIELD</span></div>
  <div class="divider"></div>
  <div class="person-role">Director</div>

  <ul class="contact-list">
    <li>
      <svg viewBox="0 0 16 16" aria-hidden="true"><path fill="var(--brand-blue)" d="M3.6 1.2l2.2 2.6-1.1 1.8c.9 2.1 2.6 3.8 4.7 4.7l1.8-1.1 2.6 2.2-1.3 2.4C6.8 13.6 2.4 9.2 1.2 2.5z"/></svg>
      5153927048
    </li>
    <li>
      <svg viewBox="0 0 16 16" aria-hidden="true"><rect x="1.5" y="3.5" width="13" height="9" rx="1" fill="none" stroke="var(--brand-blue)" stroke-width="1.5"/><path d="M1.5 4l6.5 5 6.5-5" fill="none" stroke="var(--brand-blue)" stroke-width="1.5"/></svg>
      trellbrixco@quamlet.com
    </li>
    <li>
      <svg viewBox="0 0 16 16" aria-hidden="true"><circle cx="8" cy="8" r="6.5" fill="none" stroke="var(--brand-blue)" stroke-width="1.4"/><ellipse cx="8" cy="8" rx="2.8" ry="6.5" fill="none" stroke="var(--brand-blue)" stroke-width="1.2"/><path d="M1.5 8h13M2.5 5h11M2.5 11h11" stroke="var(--brand-blue)" stroke-width="1"/></svg>
      www.trellbrixco.com
    </li>
  </ul>

  <svg class="edge-band" viewBox="0 0 700 12" preserveAspectRatio="none" aria-hidden="true">
    <polygon points="0,0 440,0 436,12 0,12" fill="var(--brand-blue)"/>
    <polygon points="446,0 700,0 700,12 442,12" fill="var(--brand-orange)"/>
  </svg>
</section>

</body>
</html>
```